Book cover - Quiet Rooms, Open Doors

Book cover for Ebook (Pagelight) and wrap around print cover (Printvale) (back, front, and spine)

The book title (may slightly change by end of brief):
(MAIN TITLE) 'Quiet Rooms, Open Doors'
(SUB HEADING) 'A Week-by-Week Practical Workbook to Loosen Nervous Habits, Quieten Doubt and Build Steady Poise'
by Dr Owen Hartley

I would like a bold, stand out cover. Contemporary. I would like to avoid stereotypical images of people looking anxious or worried. I would like the design to be more uplifting and hopeful, rather than focusing on the negative aspect of anxiety, but avoiding cliched photos of people raising their hands in the air, smiling and jumping etc. The cover should appeal to both men and women.

Trim size of book cover (for PrintVale) is 5.25" x 8" back and front with a spine size of 0.477 inches

Reason: I have decided to extend the deadline by 1 more day, not because I am unhappy with the quality of the designs, but because a few designers have contacted me to explain they have had technical difficulties when submitting their files. Thanks everyone for the hard work and great designs.

Target Market(s)

Males and females (16+) who struggle with social anxiety and shyness

Industry/Entity Type

Social

Font styles to use
Serif

Requirements
Must have
• Bold cover that is modern and contemporary. For example, I like these covers:
• http://shrtlnk.example/k4Tq9Zb
• http://shrtlnk.example/m8Wv2Hn
• http://shrtlnk.example/p3Jx6Lr
• http://shrtlnk.example/t7Gd1Qe
• http://shrtlnk.example/v2Nk8Fy
• http://shrtlnk.example/w9Bh4Cs
• http://shrtlnk.example/z5Mf3Ud
Nice to have
• Open to abstract designs.
Should not have
• No stereotypical pictures of people who look anxious or worried. Avoid cliched photos of people raising their hands in the air, smiling and jumping etc.

```html
<!DOCTYPE html>
<html lang="en">
<head>
<meta charset="utf-8">
<title>Quiet Rooms, Open Doors — Book Cover</title>
<link href="https://fonts.googleapis.com/css2?family=Bebas+Neue&family=Roboto:wght@900&display=swap" rel="stylesheet">
<style>
  :root {
    --cover-red: #cf3338;
    --splash-white: #ffffff;
    --page-bg: #ffffff;
    --frame-line: #333333;
  }
  * { margin: 0; padding: 0; box-sizing: border-box; }
  html, body {
    width: 1152px;
    height: 1200px;
    overflow: hidden;
    background: var(--page-bg);
  }
  .canvas {
    position: relative;
    width: 1152px;
    height: 1200px;
    border: 1px solid var(--frame-line);
  }
  .cover {
    position: absolute;
    left: 239px;
    top: 106px;
    width: 632px;
    height: 962px;
    background: var(--cover-red);
    overflow: hidden;
  }
  .splash {
    position: absolute;
    display: block;
  }
  .splash--title {
    left: 40px;
    top: 110px;
    width: 500px;
    height: 460px;
  }
  .splash--author {
    left: 190px;
    top: 820px;
    width: 310px;
    height: 150px;
  }
  .title {
    position: absolute;
    left: 60px;
    top: 222px;
    width: 460px;
    font-family: "Bebas Neue", "Oswald", sans-serif;
    font-weight: 400;
    font-size: 90px;
    line-height: 92px;
    letter-spacing: 1px;
    text-align: center;
    color: var(--cover-red);
  }
  .title span { display: block; }
  .subtitle {
    position: absolute;
    left: 40px;
    top: 645px;
    width: 560px;
    font-family: "Roboto", "Arial Black", sans-serif;
    font-weight: 900;
    font-size: 22px;
    line-height: 30px;
    text-align: center;
    color: var(--splash-white);
    transform: rotate(-3deg);
    transform-origin: center;
  }
  .author {
    position: absolute;
    left: 190px;
    top: 912px;
    width: 270px;
    font-family: "Roboto", "Arial Black", sans-serif;
    font-weight: 900;
    font-size: 24px;
    text-align: center;
    color: var(--cover-red);
  }
</style>
</head>
<body>
  <div class="canvas">
    <div class="cover">
      <svg class="splash splash--title" viewBox="0 0 500 460" role="img" aria-label="Abstract white burst splash with radiating streaks behind the title">
        <path d="M60 40 Q250 0 440 40 Q500 230 450 420 Q250 470 50 420 Q0 230 60 40 Z" fill="var(--splash-white)"/>
      </svg>
      <h1 class="title">
        <span>Quiet</span>
        <span>Rooms, Open</span>
        <span>Doors</span>
      </h1>
      <p class="subtitle">A Week-by-Week Practical Workbook to Loosen Nervous Habits, Quieten Doubt and Build Steady Poise</p>
      <svg class="splash splash--author" viewBox="0 0 310 150" role="img" aria-label="Abstract white burst splash rising from the bottom edge behind the author name">
        <path d="M0 150 Q20 40 150 20 Q290 40 310 150 Z" fill="var(--splash-white)"/>
      </svg>
      <p class="author">Dr Owen Hartley</p>
    </div>
  </div>
</body>
</html>
```